EPS Recycling End Market Infographic

We need a two-page visual presentation of new end-market applications for recycled expanded polystyrene (EPS) collected for recycling. This focuses on expanded polystyrene (foam) transport packaging used for international distribution of goods, including pharmaceuticals and food, electronics, appliances and other products that need superior packaging protection.

The bulletin will have examples of 5 major industry categories that benefit from recycled EPS feedstock for reverse engineering to meet current market demand. It will also showcase names of companies that use recycled content EPS in their product manufacturing to legitimize end market adoption. The capability to use recycled EPS in new EPS packaging should be highlighted. We would like this bulletin to demonstrate the widespread application of recycled EPS in different industries and establish credibility that it is being used in a variety of interesting recycled-content products. We welcome creative and interesting font treatments and new trends in graphic design.

Target Market(s)

International Government Agencies, Packaging Engineers, Big Box Retailers, & Environmental Professionals

Industry/Entity Type

Plastic Manufacturers

Font styles to use
Sans Serif

Requirements
Must have
• Visual focus points, multiple examples of products and manufacturers as evidence to the information content
Should not have
• Insufficient white space or outdated design elements (like two-tone gradients).

```html
<!DOCTYPE html>
<html lang="en">
<head>
<meta charset="utf-8">
<title>Recycling EPS End Market</title>
<link href="https://fonts.googleapis.com/css2?family=Montserrat:ital,wght@0,400;0,500;0,700;0,800;0,900;1,700;1,800&display=swap" rel="stylesheet">
<style>
  :root{
    --blue:#5d8ca9;
    --gold:#b98f0b;
    --brown:#5b2a12;
    --white:#ffffff;
    --page:#ffffff;
  }
  *{box-sizing:border-box;margin:0;padding:0}
  html,body{width:1200px;height:1200px;overflow:hidden;background:var(--page);font-family:'Montserrat',sans-serif}
  .slide{position:absolute;left:179px;width:850px;height:478px;background:var(--white);overflow:hidden;box-shadow:0 0 8px rgba(93,140,169,.25)}
  .slide--cover{top:78px}
  .slide--examples{top:651px}
  .abs{position:absolute}

  /* cover */
  .cover-title{left:34px;top:30px;line-height:1}
  .cover-title .light{display:block;color:var(--gold);font-weight:400;font-size:70px;letter-spacing:-.5px}
  .cover-title .bold{display:block;color:var(--blue);font-weight:800;font-size:68px;line-height:80px;letter-spacing:-1px}
  .cover-lede{left:36px;top:280px;width:328px;color:var(--gold);font-size:13.5px;line-height:16.6px;font-weight:500;hyphens:auto;-webkit-hyphens:auto;letter-spacing:-.1px}
  .foam-box{left:478px;top:58px;width:276px;height:340px;border-radius:26px;background:radial-gradient(ellipse at 40% 30%,#fbfbfb,#e7e9ea 75%);transform:rotate(6deg);box-shadow:0 6px 14px rgba(40,60,80,.18)}
  .stat{left:537px;top:236px;width:252px;height:125px;background:var(--white);border:1.5px solid var(--gold);border-radius:5px;padding:14px 14px 0 13px}
  .stat-num{font-weight:900;font-size:42px;color:var(--gold);line-height:1;-webkit-text-stroke:1.5px var(--brown);letter-spacing:-1px}
  .stat-unit{font-weight:800;font-size:16px;color:var(--brown);margin-left:2px}
  .stat-text{margin-top:8px;font-style:italic;font-weight:800;font-size:15.5px;line-height:19.5px;color:var(--gold)}
  .stat-text b{color:var(--brown);font-weight:800}

  .brand{display:flex;align-items:center;gap:5px}
  .brand-dot{border-radius:50%;background:var(--gold);flex:none}
  .brand-name{color:var(--brown);font-weight:500;line-height:1.05;white-space:nowrap}
  .brand--cover{left:36px;top:405px}
  .brand--cover .brand-dot{width:52px;height:52px}
  .brand--cover .brand-name{font-size:10px}
  .brand--examples{left:151px;top:440px}
  .brand--examples .brand-dot{width:32px;height:32px}
  .brand--examples .brand-name{font-size:6px}

  /* examples */
  .ex-heading{left:34px;top:25px;color:var(--white);font-weight:800;font-size:27px;line-height:34px}
  .ex-intro{left:34px;top:175px;width:205px;color:var(--white);font-size:9.6px;line-height:11.8px;hyphens:auto;-webkit-hyphens:auto}
  .sectors{left:34px;top:262px;list-style:none}
  .sectors li{display:flex;align-items:center;height:29px;color:var(--white);font-style:italic;font-weight:800;font-size:9.5px}
  .sectors svg{width:22px;height:20px;margin-right:7px;flex:none}

  .product{border-radius:14px;box-shadow:0 8px 12px -6px rgba(0,0,0,.18)}
  .tag{background:var(--gold);color:var(--white);font-weight:700;font-size:9.5px;line-height:11px;text-align:center;border-radius:7px;display:flex;align-items:center;justify-content:center;padding:0 5px;z-index:2}
  .maker{border:1.3px solid var(--blue);border-radius:4px;background:var(--white);color:var(--blue);font-weight:700;text-align:right;padding:2px 4px 1px 10px;line-height:1.05;white-space:nowrap;z-index:2}
  .maker::before{content:"by:";position:absolute;right:4px;top:-9px;font-size:6px;font-style:italic;font-weight:800;color:var(--white);background:var(--blue);padding:1px 4px;border-radius:3px 3px 0 0}
</style>
</head>
<body>

<section class="slide slide--cover">
  <svg class="abs" style="left:0;top:0" width="850" height="478" viewBox="0 0 850 478">
    <polygon points="661,0 850,0 850,478 538,478" fill="var(--blue)"/>
    <polygon points="637,0 661,0 538,478 515,478" fill="var(--gold)"/>
  </svg>
  <h1 class="abs cover-title"><span class="light">Recycling</span><span class="bold">EPS End</span><span class="bold">Market</span></h1>
  <p class="abs cover-lede">From cold chain shipping containers to protective foam packaging components and bracing inserts, EPS applications can use 30-50% recycled content.</p>
  <div class="abs foam-box" role="img" aria-label="White expanded polystyrene shipping container"></div>
  <div class="abs stat">
    <div><span class="stat-num">30,000</span><span class="stat-unit">TONS</span></div>
    <p class="stat-text"><b>of</b> expanded Polystyrene (EPS) <b>was recycled in</b> 2024</p>
  </div>
  <div class="abs brand brand--cover"><span class="brand-dot"></span><span class="brand-name">Foam Loop<br>Alliance</span></div>
</section>

<section class="slide slide--examples">
  <svg class="abs" style="left:0;top:0" width="850" height="478" viewBox="0 0 850 478">
    <polygon points="0,0 338,0 234,405 0,478" fill="var(--blue)"/>
    <polygon points="234,405 314,478 216,478" fill="var(--gold)"/>
  </svg>
  <h2 class="abs ex-heading">Examples of<br>Companies<br>that use our<br>products</h2>
  <p class="abs ex-intro">Recycled EPS foam can be repurposed into a diverse array of products across various industries. These applications underscore the versatility of recycled EPS, contributing to sustainability across multiple sectors, such as:</p>
  <ul class="abs sectors">
    <li><svg viewBox="0 0 22 20" fill="none" stroke="#fff" stroke-width="1.6"><path d="M3 19V2h4v17M1 4h16M14 4v5M9 19v-7h10v7M1 19h20"/></svg>Construction &amp; Architecture</li>
    <li><svg viewBox="0 0 22 20" fill="none" stroke="#fff" stroke-width="1.6"><rect x="2" y="6" width="5" height="12"/><rect x="9" y="3" width="5" height="15"/><rect x="16" y="6" width="5" height="12"/><path d="M2 10h5M9 8h5M16 10h5"/></svg>Textile &amp; Fiber</li>
    <li><svg viewBox="0 0 22 20" fill="none" stroke="#fff" stroke-width="1.6"><path d="M2 7l9-5 9 5-9 5zM2 7v8l9 5 9-5V7M11 12v8"/></svg>Wood Composites &amp; Blends</li>
    <li><svg viewBox="0 0 22 20" fill="none" stroke="#fff" stroke-width="1.6"><path d="M5 3h12v15H5zM5 3c0-1 12-1 12 0M9 8v6M13 10v4"/></svg>Paints, Coatings &amp; Adhesives</li>
    <li><svg viewBox="0 0 22 20"><circle cx="11" cy="10" r="9" fill="#fff"/><path d="M11 5v10M6 10h10" stroke="var(--blue)" stroke-width="2"/></svg>Additives</li>
  </ul>
  <div class="abs brand brand--examples"><span class="brand-dot"></span><span class="brand-name">Foam Loop<br>Alliance</span></div>

  <div class="abs product" style="left:332px;top:104px;width:98px;height:82px;background:linear-gradient(160deg,#4d4d4d,#1c1c1c)" role="img" aria-label="Black automotive battery housing component"></div>
  <div class="abs tag" style="left:372px;top:75px;width:87px;height:31px">AUTOMOTIVE<br>COMPONENTS</div>
  <div class="abs maker" style="right:390px;top:160px;font-size:7.5px">NORTHFOLD</div>

  <div class="abs product" style="left:500px;top:104px;width:110px;height:84px;background:linear-gradient(160deg,#86a8c1,#5f87a4)" role="img" aria-label="Blue slatted patio bench"></div>
  <div class="abs tag" style="left:592px;top:75px;width:57px;height:31px">PATIO<br>BENCH</div>
  <div class="abs maker" style="right:192px;top:160px;font-size:7px">CEDAR 88</div>

  <div class="abs product" style="left:686px;top:92px;width:90px;height:84px;background:linear-gradient(135deg,#444,#141414)" role="img" aria-label="Black plastic fork and spoon"></div>
  <div class="abs tag" style="left:716px;top:75px;width:55px;height:19px">SPOON</div>
  <div class="abs maker" style="right:18px;top:160px;font-size:5.4px;padding-top:3px;padding-bottom:2px">GREENWARE GOODS</div>

  <div class="abs product" style="left:315px;top:246px;width:55px;height:178px;border-radius:50% 50% 45% 45%/40% 40% 12% 12%;background:linear-gradient(90deg,#f5f5f5,#e2e2e2)" role="img" aria-label="White foam surfboard blank"></div>
  <div class="abs tag" style="left:364px;top:278px;width:84px;height:31px">SURFBOARD<br>BLANKS</div>
  <div class="abs maker" style="right:422px;top:362px;font-size:6.5px;padding-top:2px">CRESTLINE FOAM</div>

  <div class="abs product" style="left:490px;top:280px;width:144px;height:124px;background:linear-gradient(160deg,#b08a6c,#7d5a43)" role="img" aria-label="Wooden-look clothing hangers"></div>
  <div class="abs tag" style="left:568px;top:278px;width:86px;height:31px">CLOTHING<br>HANGERS</div>
  <div class="abs maker" style="right:211px;top:370px;font-size:8.5px">ARBORA</div>

  <div class="abs product" style="left:703px;top:305px;width:77px;height:100px;background:linear-gradient(160deg,#cfbda2,#9c8467)" role="img" aria-label="Wood-effect picture frame"></div>
  <div class="abs tag" style="left:745px;top:278px;width:58px;height:31px">PICTURE<br>FRAME</div>
  <div class="abs maker" style="right:27px;top:362px;font-size:6px;text-align:left">KESTREL<br>RECYCLING</div>
</section>

</body>
</html>
```